AI Business Tools Landing Page

My web-based website builder (Nurvanta.com) will be adding many new features in the very near future and I need an eye-catching landing page to promote these new products.

The page will have a primary section of the 8 main products we are promoting:
1. AI Instant Website Generator
2. AI Chatbot
3. Online Store Builder with AI Assistance
4. AI Auto-Blogging System
5. Online Scheduling System
6. Custom Email System
7. SEO Service
8. CRM System

The page will also have a smaller section for links to our affiliate programs. These can be smaller, less-promanent buttons or links. These are the affiliate products:
1. Get Your LLC
2. Website Design and Maintenance
3. Tavolin Ads Management
4. Social Media Posting Service
5. Logo Design
6. Trademark Registration
7. Patent Application
8. Printing Services (including postcards, flyers, and merch.)
9. Bulk AI Content Generator

The theme and color scheme of the page should follow the theme of our main website, which is https://nurvanta.com.

I need the page fully coded and ready to deploy on my server.

I look forward to seeing your amazing designs!

```html
<!DOCTYPE html>
<html lang="en">
<head>
<meta charset="utf-8">
<title>Nurvanta – AI Business Tools</title>
<link href="https://fonts.googleapis.com/css2?family=Quicksand:wght@400;500;600;700&family=Lato:wght@400;700&display=swap" rel="stylesheet">
<style>
:root{
  --blue:#1a95e0;
  --blue-dark:#0f7fcf;
  --navy:#0b1f4d;
  --ink:#1d2a4a;
  --text:#3a4560;
  --muted:#5f6880;
  --line:#dde3ec;
  --soft:#eef1f6;
  --footer:#0d1b36;
  --white:#ffffff;
}
*{box-sizing:border-box;margin:0;padding:0}
html,body{width:1200px;height:2365px;overflow:hidden}
body{position:relative;background:var(--white);font-family:'Lato',sans-serif;color:var(--text)}
.abs{position:absolute}

/* header */
.site-header{position:absolute;left:0;top:0;width:1200px;height:73px;background:var(--white);border-bottom:1px solid var(--line)}
.brand{position:absolute;left:92px;top:18px;display:flex;align-items:center;gap:10px;font-family:'Quicksand',sans-serif;font-weight:700;font-size:25px;color:var(--ink)}
.brand-dot{width:34px;height:34px;border-radius:50%;background:var(--blue)}
.main-nav{position:absolute;left:365px;top:27px;display:flex;gap:25px;font-size:14.5px;color:var(--ink)}
.btn-start{position:absolute;left:1005px;top:15px;width:143px;height:42px;border-radius:6px 14px 6px 6px;background:var(--blue);color:var(--white);font-size:15px;display:flex;align-items:center;justify-content:center}

/* hero */
.hero{position:absolute;left:0;top:73px;width:1200px;height:715px}
.hero-copy{position:absolute;left:143px;top:112px;color:var(--white)}
.hero-title{font-family:'Quicksand',sans-serif;font-weight:500;font-size:41px;line-height:53px}
.hero-title b{font-weight:700}
.hero-text{margin-top:20px;width:430px;font-size:17.5px;line-height:25px}

/* features */
.section-title{position:absolute;left:0;width:1200px;text-align:center;font-family:'Quicksand',sans-serif;font-size:40px;color:var(--ink);font-weight:500}
.section-title .accent{color:var(--blue);font-weight:700}
.section-title b{font-weight:700}
.section-sub{position:absolute;left:0;width:1200px;text-align:center;font-size:18.5px;color:var(--muted)}
.rule{position:absolute;left:545px;width:110px;height:3px;background:var(--blue)}

.card{position:absolute;width:250px;height:261px;background:var(--white);border:1px solid var(--line);border-radius:4px;box-shadow:0 2px 8px rgba(20,40,80,.06);padding:28px 22px 0 27px}
.card .icon{width:80px;height:60px;margin-bottom:18px}
.card h3{font-family:'Quicksand',sans-serif;font-weight:700;font-size:18.5px;line-height:21px;color:var(--ink);margin-bottom:12px}
.card p{font-family:'Quicksand',sans-serif;font-size:14px;line-height:19.5px;color:var(--text)}
.card .go{position:absolute;right:17px;bottom:17px;width:25px;height:25px}
.card.active{background:var(--blue);border-color:var(--blue);box-shadow:0 8px 20px rgba(26,149,224,.35)}
.card.active h3,.card.active p{color:var(--white)}

.btn-pill{position:absolute;height:46px;border-radius:6px 14px 6px 6px;background:linear-gradient(110deg,var(--blue) 55%,var(--blue-dark) 55%);color:var(--white);font-size:19px;display:flex;align-items:center;justify-content:center}

/* tools */
.tools{position:absolute;left:0;top:1664px;width:1200px;height:624px;background:var(--soft)}
.tool{position:absolute;width:212px;height:81px;background:var(--white);border-radius:8px;box-shadow:0 3px 10px rgba(20,40,80,.08);display:flex;align-items:center;justify-content:center;text-align:center;font-family:'Quicksand',sans-serif;font-size:17px;line-height:21px;color:var(--ink);font-weight:500}
.tool.active{background:var(--blue);color:var(--white);border:1px solid var(--blue-dark)}

.site-footer{position:absolute;left:0;top:2288px;width:1200px;height:77px;background:var(--footer);display:flex;align-items:center;justify-content:center;font-family:'Quicksand',sans-serif;font-size:16px;color:#7d8aa8}
</style>
</head>
<body>

<header class="site-header">
  <div class="brand"><span class="brand-dot"></span>Nurvanta</div>
  <nav class="main-nav">
    <span>About Us</span><span>Learn More</span><span>Make Money</span><span>History of AI</span><span>Pricing</span><span>Blog</span>
  </nav>
  <a class="btn-start">Get Started</a>
</header>

<section class="hero">
  <svg width="1200" height="715" viewBox="0 73 1200 715" class="abs" style="left:0;top:0">
    <defs>
      <linearGradient id="heroFill" x1="0" y1="0" x2="1" y2="1">
        <stop offset="0" stop-color="#0a1a44"/>
        <stop offset="0.55" stop-color="#0d3a7a"/>
        <stop offset="1" stop-color="#0a1e4c"/>
      </linearGradient>
      <radialGradient id="heroGlow" cx="0.72" cy="0.4" r="0.35">
        <stop offset="0" stop-color="#2f7fd0" stop-opacity=".6"/>
        <stop offset="1" stop-color="#2f7fd0" stop-opacity="0"/>
      </radialGradient>
    </defs>
    <polygon fill="var(--blue)" points="0,73 1200,73 1200,532 1111,583 1106,633 410,785 142,633 115,633 0,532"/>
    <g role="img" aria-label="Digital figure made of glowing network points working at a computer">
      <polygon fill="url(#heroFill)" points="0,73 1200,73 1200,520 1100,575 1095,622 410,773 142,622 115,622 0,520"/>
      <polygon fill="url(#heroGlow)" points="0,73 1200,73 1200,520 1100,575 1095,622 410,773 142,622 115,622 0,520"/>
    </g>
  </svg>
  <div class="hero-copy">
    <h1 class="hero-title">Create a website<br>with <b>Nurvanta</b><br><b>AI Website Builder</b></h1>
    <p class="hero-text">Halvorn Consulting provides decades of experience implementing Corvex EPM products with unique and innovative solutions to challenging business...</p>
  </div>
</section>

<h2 class="section-title" style="top:838px"><span class="accent">Additional Features</span> for your website</h2>
<p class="section-sub" style="top:898px">Lorem Ipsum is simply dummy text of the printing and typesetting</p>
<div class="rule" style="top:942px"></div>

<!-- card icons use simple line shapes -->
<article class="card" style="left:87px;top:984px">
  <svg class="icon" viewBox="0 0 80 60"><circle cx="60" cy="32" r="20" fill="#e8ecf3"/><g fill="none" stroke="var(--blue)" stroke-width="2.2"><path d="M10 38a10 10 0 0 1 4-19 14 14 0 0 1 27 2 9 9 0 0 1 2 17z"/><circle cx="31" cy="30" r="5"/><path d="M31 21v3M31 36v3M22 30h3M37 30h3"/></g></svg>
  <h3>AI Instant Website Generator</h3>
  <p>Lorem Ipsum is simply dummy text of the printing</p>
  <svg class="go" viewBox="0 0 26 26"><circle cx="13" cy="13" r="11.5" fill="none" stroke="var(--blue)" stroke-width="1.5"/><path d="M7 13h11M14 9l4 4-4 4" fill="none" stroke="var(--blue)" stroke-width="1.6"/></svg>
</article>

<article class="card active" style="left:346px;top:969px">
  <svg class="icon" viewBox="0 0 80 60"><circle cx="60" cy="28" r="20" fill="#3aa8e8"/><g fill="none" stroke="#fff" stroke-width="2.2"><rect x="2" y="4" width="52" height="40" rx="3"/><path d="M2 36h52M22 44v8M14 52h28M22 17l-5 5 5 5M34 17l5 5-5 5M30 14l-4 16"/></g></svg>
  <h3>AI Chatbot</h3>
  <p>Lorem Ipsum is simply dummy text of the printing</p>
  <svg class="go" viewBox="0 0 26 26"><circle cx="13" cy="13" r="11.5" fill="none" stroke="#fff" stroke-width="1.5"/><path d="M7 13h11M14 9l4 4-4 4" fill="none" stroke="#fff" stroke-width="1.6"/></svg>
</article>

<article class="card" style="left:604px;top:984px">
  <svg class="icon" viewBox="0 0 80 60"><circle cx="58" cy="32" r="20" fill="#e8ecf3"/><g fill="none" stroke="var(--blue)" stroke-width="2.2"><circle cx="34" cy="20" r="12"/><circle cx="34" cy="17" r="4"/><path d="M26 28a9 9 0 0 1 16 0M4 40l12-8 10 4 10-4 12 8-18 12z"/></g></svg>
  <h3>Online Store Builder with AI Assistance</h3>
  <p>Lorem Ipsum is simply dummy text of the printing</p>
  <svg class="go" viewBox="0 0 26 26"><circle cx="13" cy="13" r="11.5" fill="none" stroke="var(--blue)" stroke-width="1.5"/><path d="M7 13h11M14 9l4 4-4 4" fill="none" stroke="var(--blue)" stroke-width="1.6"/></svg>
</article>

<article class="card" style="left:862px;top:984px">
  <svg class="icon" viewBox="0 0 80 60"><circle cx="54" cy="32" r="20" fill="#e8ecf3"/><g fill="none" stroke="var(--blue)" stroke-width="2.6"><path d="M44 28V4H4v54h28"/><path d="M12 16h24M12 26h24M12 36h14M34 46l6 8 12-18"/></g></svg>
  <h3>AI Auto-Blogging System</h3>
  <p>Lorem Ipsum is simply dummy text of the printing</p>
  <svg class="go" viewBox="0 0 26 26"><circle cx="13" cy="13" r="11.5" fill="none" stroke="var(--blue)" stroke-width="1.5"/><path d="M7 13h11M14 9l4 4-4 4" fill="none" stroke="var(--blue)" stroke-width="1.6"/></svg>
</article>

<article class="card" style="left:87px;top:1256px">
  <svg class="icon" viewBox="0 0 80 60"><circle cx="56" cy="30" r="20" fill="#e8ecf3"/><g fill="none" stroke="var(--blue)" stroke-width="2.2"><rect x="22" y="20" width="14" height="14"/><rect x="2" y="20" width="10" height="10"/><rect x="46" y="20" width="10" height="10"/><rect x="24" y="2" width="10" height="10"/><rect x="24" y="44" width="10" height="10"/><rect x="6" y="4" width="8" height="8"/><rect x="44" y="4" width="8" height="8"/><rect x="6" y="44" width="8" height="8"/><rect x="44" y="44" width="8" height="8"/><path d="M12 25h10M36 25h10M29 12v8M29 34v10"/></g></svg>
  <h3>Online Scheduling System</h3>
  <p>Lorem Ipsum is simply dummy text of the printing</p>
  <svg class="go" viewBox="0 0 26 26"><circle cx="13" cy="13" r="11.5" fill="none" stroke="var(--blue)" stroke-width="1.5"/><path d="M7 13h11M14 9l4 4-4 4" fill="none" stroke="var(--blue)" stroke-width="1.6"/></svg>
</article>

<article class="card" style="left:346px;top:1256px">
  <svg class="icon" viewBox="0 0 80 60"><circle cx="58" cy="30" r="20" fill="#e8ecf3"/><g fill="none" stroke="var(--blue)" stroke-width="2.2"><rect x="0" y="2" width="56" height="42" rx="2"/><rect x="8" y="10" width="10" height="8"/><rect x="23" y="10" width="10" height="8"/><rect x="38" y="10" width="10" height="8"/><rect x="8" y="24" width="16" height="8"/><rect x="30" y="24" width="18" height="8"/><path d="M0 36h56M22 44l-4 12M34 44l4 12M14 56h28"/></g></svg>
  <h3>Custom Email System</h3>
  <p>Lorem Ipsum is simply dummy text of the printing</p>
  <svg class="go" viewBox="0 0 26 26"><circle cx="13" cy="13" r="11.5" fill="none" stroke="var(--blue)" stroke-width="1.5"/><path d="M7 13h11M14 9l4 4-4 4" fill="none" stroke="var(--blue)" stroke-width="1.6"/></svg>
</article>

<article class="card" style="left:604px;top:1256px">
  <svg class="icon" viewBox="0 0 80 60"><circle cx="54" cy="28" r="20" fill="#e8ecf3"/><g fill="none" stroke="var(--blue)" stroke-width="2.2"><circle cx="34" cy="24" r="20"/><circle cx="34" cy="24" r="15"/><path d="M20 38L4 54"/></g><text x="34" y="29" text-anchor="middle" font-family="Quicksand,sans-serif" font-size="13" font-weight="700" fill="var(--blue)">SEO</text></svg>
  <h3>SEO Service</h3>
  <p>Lorem Ipsum is simply dummy text of the printing</p>
  <svg class="go" viewBox="0 0 26 26"><circle cx="13" cy="13" r="11.5" fill="none" stroke="var(--blue)" stroke-width="1.5"/><path d="M7 13h11M14 9l4 4-4 4" fill="none" stroke="var(--blue)" stroke-width="1.6"/></svg>
</article>

<article class="card" style="left:862px;top:1256px">
  <svg class="icon" viewBox="0 0 80 60"><circle cx="54" cy="28" r="20" fill="#e8ecf3"/><g fill="none" stroke="var(--blue)" stroke-width="2.2"><path d="M6 38a24 24 0 1 1 48 0"/><circle cx="30" cy="24" r="6"/><rect x="4" y="40" width="48" height="16" rx="3"/></g><text x="28" y="53" text-anchor="middle" font-family="Quicksand,sans-serif" font-size="13" font-weight="700" fill="var(--blue)">CRM</text></svg>
  <h3>CRM System</h3>
  <p>Lorem Ipsum is simply dummy text of the printing</p>
  <svg class="go" viewBox="0 0 26 26"><circle cx="13" cy="13" r="11.5" fill="none" stroke="var(--blue)" stroke-width="1.5"/><path d="M7 13h11M14 9l4 4-4 4" fill="none" stroke="var(--blue)" stroke-width="1.6"/></svg>
</article>

<a class="btn-pill" style="left:495px;top:1552px;width:210px">Additional Features</a>

<section class="tools">
  <h2 class="section-title" style="top:60px;line-height:52px">More tools to help <b>your grow<br>your business</b></h2>
  <div class="rule" style="top:174px"></div>

  <a class="tool" style="left:266px;top:207px">Get Your LLC</a>
  <a class="tool active" style="left:494px;top:207px">Website Design<br>and Maintenance</a>
  <a class="tool" style="left:722px;top:207px">Tavolin Ads<br>Management</a>
  <a class="tool" style="left:266px;top:304px">Social Media<br>Posting Service</a>
  <a class="tool" style="left:494px;top:304px">Logo Design</a>
  <a class="tool" style="left:722px;top:304px">Trademark<br>Registration</a>
  <a class="tool" style="left:266px;top:401px">Patent Application</a>
  <a class="tool" style="left:494px;top:401px">Printing Services</a>
  <a class="tool" style="left:722px;top:401px">Bulk AI Content<br>Generator</a>

  <a class="btn-pill" style="left:517px;top:518px;width:166px">More Tools</a>
</section>

<footer class="site-footer">Copyright © nurvanta 2024. All rights reserved. | Privacy Policy</footer>

</body>
</html>
```